Layout for new page on existing website

We have an existing website (www.brightloomworks.org) and need a new page designing to promote a new product.
The new page needs to be consistent with the existing website look and feel (www.brightloomworks.org) but current persistent elements on the standard page design can be moved/removed from the page to accommodate a new layout necessary for getting all the content laid out in a logical user friendly way.
The content required for the page is attached along with a wireframe mock up that may help understand the expectation, however the wireframe was just created to help me work out what was needed on the page and the layout can be different. A key element is the quality of the design of each of the artifacts (e.g. the panel the embedded video needs to go in, icons etc) and a clear display of the information.
Updates
The website that the new page needs to fit into is www.brightloomworks.org, i will also added the company logo to the brief.
Our Corporate Colours
- Green: #A2FF00
- Cream: #FFFF99
- Yellow: #FFE900
- Grey: #534741
Industry/Entity Type
Product
Look and feel
Each slider illustrates characteristics of the customer's brand and the style your logo design should communicate.

```html
<!DOCTYPE html>
<html lang="en">
<head>
<meta charset="utf-8">
<title>Brightloom Works – Course Management and Booking</title>
<link rel="stylesheet" href="https://fonts.googleapis.com/css2?family=Open+Sans:wght@400;600;700&display=swap">
<style>
:root{
  --bg:#4e443f;
  --bg-dark:#3f3632;
  --green:#a2ff00;
  --lime:#d9ee2c;
  --cream:#ffff99;
  --yellow:#ffe900;
  --text:#f1eee6;
  --muted:#a79d95;
  --field:#625752;
  --field-line:#7a6f69;
  --shadow:#3a312d;
}
*{box-sizing:border-box;margin:0;padding:0}
html,body{width:1200px;height:3315px;overflow:hidden}
body{background:var(--bg);font-family:"Open Sans",Arial,sans-serif;color:var(--text);position:relative}
.abs{position:absolute}

/* side navigation */
.side-nav{left:114px;top:0;width:150px;height:960px}
.side-nav a{position:absolute;left:0;width:150px;text-align:center;color:var(--text);text-decoration:none;font-size:14px;line-height:18px;font-weight:600}
.side-nav svg{display:block;margin:0 auto 6px;width:56px;height:56px}
.nav-rule{left:264px;top:195px;width:6px;height:795px;background:linear-gradient(90deg,rgba(0,0,0,.3),rgba(0,0,0,0))}

/* header */
.brand{left:330px;top:86px;width:660px;text-align:center;font-weight:700;font-size:40px;line-height:50px;letter-spacing:6px;color:#fff;white-space:nowrap}
.brand .dot{display:inline-block;width:28px;height:28px;border-radius:50%;background:var(--green);vertical-align:middle;margin:0 12px 6px 6px}
.tagline{left:330px;top:194px;width:660px;text-align:center;color:var(--lime);font-size:24px;line-height:32px;font-weight:600;white-space:nowrap}

/* hero banner */
.hero{left:324px;top:249px;width:675px;height:237px;border-radius:12px;background:linear-gradient(180deg,#6e655f 0,#4a413c 27%,#b4f000 27%,#94d400 100%);overflow:hidden;box-shadow:0 12px 20px rgba(0,0,0,.3)}
.hero h2{position:absolute;left:18px;top:108px;width:280px;font-size:32px;line-height:44px;font-weight:600;color:#1b2400}
.hero-shots{position:absolute;right:8px;top:12px;width:370px;height:212px;border-radius:8px;background:linear-gradient(135deg,#e6ecef,#8da4b3 55%,#2c3238)}

/* video + testimonial */
.video{left:324px;top:573px;width:336px;height:336px;background:#000;box-shadow:0 10px 18px rgba(0,0,0,.35)}
.video-bar{position:absolute;left:0;right:0;bottom:0;height:24px;background:linear-gradient(#e6e6e6,#bcbcbc)}
.video-bar i{position:absolute;top:6px;width:12px;height:12px;background:#555}
.video-bar .red{background:#c61d1d}
.spinner{position:absolute;left:159px;top:150px;width:18px;height:18px;border:3px dotted #ccc;border-radius:50%}
.quote-mark{font-size:160px;line-height:1;color:var(--shadow);font-family:Georgia,serif;font-weight:700}
.quote{left:702px;top:620px;width:335px;font-size:20px;line-height:27px;color:#fff}
.cite{left:666px;top:846px;width:318px;text-align:right;font-size:13px;line-height:18px;color:#fff}
.cite span{color:var(--lime)}

/* sections */
.section-title{font-size:28px;line-height:36px;color:var(--lime);font-weight:400}
.feature{width:300px;font-size:16px;line-height:21px;color:var(--text)}
.feature svg{float:left;width:96px;height:110px;margin:0 12px 4px 0}
.feature h3{font-size:16px;line-height:21px;font-weight:600;color:var(--lime)}

.benefits{left:366px;top:2058px;width:570px;list-style:none}
.benefits li{position:relative;padding-left:36px;font-size:15px;line-height:20px;margin-bottom:20px}
.benefits li svg{position:absolute;left:0;top:0;width:20px;height:20px}

/* contact form */
.contact-title{left:369px;top:2728px;width:520px;font-size:27px;line-height:36px;font-weight:400;color:var(--lime)}
.form-row{left:369px;width:558px;height:36px}
.form-row label{position:absolute;left:0;top:6px;font-size:17px;line-height:24px;color:#fff}
.form-row .field{position:absolute;left:120px;top:0;width:438px;height:36px;background:var(--field);border:1px solid var(--field-line);border-radius:3px}
.submit{left:489px;top:3060px;width:177px;height:60px;border-radius:12px;background:linear-gradient(#c8ff4a,#7cc400);color:#1d2500;font-size:24px;font-weight:700;text-align:center;line-height:60px;box-shadow:0 6px 10px rgba(0,0,0,.3)}
.footer{left:330px;top:3204px;width:660px;text-align:center;font-size:12px;line-height:16px;color:var(--muted)}
.footer-mark{left:990px;top:3196px;width:30px;height:30px}
</style>
</head>
<body>

<nav class="side-nav abs" aria-label="Main">
  <a style="top:66px">
    <svg viewBox="0 0 60 60" fill="none" stroke="#d9ee2c" stroke-width="3.5" stroke-linejoin="round"><path d="M8 30 30 10 52 30"/><path d="M15 26v24h30V26"/><path d="M25 50V36h10v14"/></svg>Home</a>
  <a style="top:228px">
    <svg viewBox="0 0 60 60" fill="none" stroke="#d9ee2c" stroke-width="3.5" stroke-linejoin="round"><path d="M30 6l7 16 17 1-13 11 4 17-15-9-15 9 4-17L6 23l17-1z"/></svg>About Us</a>
  <a style="top:348px">
    <svg viewBox="0 0 60 60" fill="none" stroke="#d9ee2c" stroke-width="3.5" stroke-linejoin="round"><path d="M8 28 52 10 40 50 30 34z"/><path d="M30 34 52 10"/></svg>Our Services</a>
  <a style="top:468px">
    <svg viewBox="0 0 60 60" fill="none" stroke="#d9ee2c" stroke-width="3.5"><circle cx="30" cy="30" r="22"/><circle cx="22" cy="24" r="2" fill="#d9ee2c"/><circle cx="38" cy="24" r="2" fill="#d9ee2c"/><path d="M19 35q11 12 22 0"/></svg>Portfolio</a>
  <a style="top:588px">
    <svg viewBox="0 0 60 60" fill="none" stroke="#d9ee2c" stroke-width="3.5" stroke-linejoin="round"><path d="M8 28h10v24H8z"/><path d="M18 30l10-20q6 0 5 9l-2 9h18q4 2 2 7l-5 15q-1 2-4 2H18"/></svg>Product</a>
  <a style="top:708px">
    <svg viewBox="0 0 60 60" fill="none" stroke="#d9ee2c" stroke-width="3.5" stroke-linejoin="round"><path d="M8 12h44v28H26L14 50V40H8z"/><path d="M16 22h28M16 30h20"/></svg>Testimonials</a>
  <a style="top:828px">
    <svg viewBox="0 0 60 60" fill="none" stroke="#d9ee2c" stroke-width="3.5" stroke-linejoin="round"><path d="M6 22q24-16 48 0l-4 6-9-3v-5H19v5l-9 3z"/><path d="M14 30h32l4 20H10z"/><circle cx="30" cy="40" r="5"/></svg>Contact Us</a>
</nav>
<div class="nav-rule abs"></div>

<header>
  <div class="brand abs">BRIGHTLOOM<span class="dot"></span>WORKS</div>
  <p class="tagline abs">Course Management and Booking Simplified</p>
</header>

<section class="hero abs">
  <h2>Built with your business in mind</h2>
  <div class="hero-shots" role="img" aria-label="Screenshots of the booking system on laptop and tablet screens"></div>
</section>

<div class="video abs" role="img" aria-label="Embedded product video player">
  <div class="spinner"></div>
  <div class="video-bar"><i style="left:8px"></i><i style="left:220px"></i><i class="red" style="left:240px"></i><i style="left:262px"></i><i class="red" style="left:284px"></i><i style="left:310px"></i></div>
</div>

<div class="quote-mark abs" style="left:676px;top:548px">“</div>
<div class="quote-mark abs" style="left:950px;top:822px">”</div>
<blockquote class="quote abs">“A convenient tool that was simple to integrate into our website. It has allowed both the business and our customers an easy way to book courses. In life sometimes simple is good and this is a great example!”</blockquote>
<p class="cite abs">Clara Denholm, Director @ Tutorlane<br><span>www.tutorlane.org</span></p>

<h2 class="section-title abs" style="left:369px;top:990px">Key Features:</h2>

<div class="feature abs" style="left:366px;top:1056px">
  <svg viewBox="0 0 96 110" fill="none" stroke="#d9ee2c" stroke-width="4"><circle cx="48" cy="46" r="34"/><path d="M48 24v22h16"/><ellipse cx="48" cy="100" rx="40" ry="6" fill="#3a312d" stroke="none"/></svg>
  <h3>Available and easy to use 24/7</h3>
  By allowing booking and payment at any time of the day, your attendees will be more likely to commit to your event and with no account setup or password required and no paper forms to fill in and post, booking onto and paying for your courses is easy.
</div>
<div class="feature abs" style="left:690px;top:1056px">
  <svg viewBox="0 0 96 110" fill="none" stroke="#d9ee2c" stroke-width="4"><rect x="38" y="8" width="18" height="34" rx="9" transform="rotate(30 47 25)"/><rect x="40" y="46" width="18" height="34" rx="9" transform="rotate(30 49 63)"/><ellipse cx="48" cy="100" rx="40" ry="6" fill="#3a312d" stroke="none"/></svg>
  <h3>Online Course promotion</h3>
  List your upcoming courses in a clear and simple way so people can easily find and select the course that suits them.
</div>
<div class="feature abs" style="left:366px;top:1347px">
  <svg viewBox="0 0 96 110" fill="none" stroke="#d9ee2c" stroke-width="4" stroke-linejoin="round"><path d="M48 10 84 78H12z"/><path d="M48 34v24M40 42h14"/><ellipse cx="48" cy="100" rx="40" ry="6" fill="#3a312d" stroke="none"/></svg>
  <h3>Online &amp; Offline Payments</h3>
  Take payments online, whilst having the flexibility of managing and adding offline payments.
</div>
<div class="feature abs" style="left:690px;top:1347px">
  <svg viewBox="0 0 96 110" fill="none" stroke="#d9ee2c" stroke-width="4" stroke-linejoin="round"><path d="M14 34 66 14l16 42-52 20z"/><path d="M14 34l36 16 16-36"/><ellipse cx="48" cy="100" rx="40" ry="6" fill="#3a312d" stroke="none"/></svg>
  <h3>Built in email system</h3>
  Enable quick and easy communication with upcoming course candidates and promotion of additional courses to past candidates.
</div>
<div class="feature abs" style="left:366px;top:1548px">
  <svg viewBox="0 0 96 110" fill="none" stroke="#d9ee2c" stroke-width="4" stroke-linejoin="round"><path d="M62 10l12 8-38 56-14 6 2-16z"/><path d="M24 64l12 10"/><ellipse cx="48" cy="100" rx="40" ry="6" fill="#3a312d" stroke="none"/></svg>
  <h3>Customisable look and feel</h3>
  All elements of the booking systems design will fit in with your existing websites style.
</div>
<div class="feature abs" style="left:690px;top:1548px">
  <svg viewBox="0 0 96 110" fill="none" stroke="#d9ee2c" stroke-width="4" stroke-linejoin="round"><rect x="14" y="14" width="60" height="60" rx="6"/><path d="M26 44l14 14 28-30"/><ellipse cx="48" cy="100" rx="40" ry="6" fill="#3a312d" stroke="none"/></svg>
  <h3>Live course place availability</h3>
  By defining minimum and maximum candidates permitted on a course its easy to prevent overbooking and also prevent courses running that don't have enough candidates.
</div>
<div class="feature abs" style="left:366px;top:1806px">
  <svg viewBox="0 0 96 110" fill="none" stroke="#d9ee2c" stroke-width="4" stroke-linejoin="round"><rect x="18" y="12" width="46" height="64" rx="4"/><path d="M28 28h26M28 40h26M28 52h16"/><path d="M72 20l8 6-16 30-6 2 1-7z"/><ellipse cx="48" cy="100" rx="40" ry="6" fill="#3a312d" stroke="none"/></svg>
  <h3>Venue database management</h3>
  Easily add, edit and remove venues from which you operate your courses from.
</div>

<h2 class="section-title abs" style="left:369px;top:1998px">Key Benefits:</h2>

<ul class="benefits abs">
  <li><svg viewBox="0 0 22 22"><path d="M3 11l5 6L19 4" fill="none" stroke="#a2ff00" stroke-width="4"/></svg>Live Availability - Availability on course place availability to prevent overbooking</li>
  <li><svg viewBox="0 0 22 22"><path d="M3 11l5 6L19 4" fill="none" stroke="#a2ff00" stroke-width="4"/></svg>Customers can search for Courses and Book Online with immediate confirmation</li>
  <li><svg viewBox="0 0 22 22"><path d="M3 11l5 6L19 4" fill="none" stroke="#a2ff00" stroke-width="4"/></svg>Automated confirmation emails</li>
  <li><svg viewBox="0 0 22 22"><path d="M3 11l5 6L19 4" fill="none" stroke="#a2ff00" stroke-width="4"/></svg>Be available for business 24/7 and take orders anytime! Customers can book when it's most convenient for them - be it early morning, late evening or weekend</li>
  <li><svg viewBox="0 0 22 22"><path d="M3 11l5 6L19 4" fill="none" stroke="#a2ff00" stroke-width="4"/></svg>No fielding phone calls, no wading through paper registrations. Attendees book on your website, there and then</li>
  <li><svg viewBox="0 0 22 22"><path d="M3 11l5 6L19 4" fill="none" stroke="#a2ff00" stroke-width="4"/></svg>No more trips to the bank, take immediate and secure payments online</li>
  <li><svg viewBox="0 0 22 22"><path d="M3 11l5 6L19 4" fill="none" stroke="#a2ff00" stroke-width="4"/></svg>Automated confirmation emails so reducing the time need communicating with candidates</li>
  <li><svg viewBox="0 0 22 22"><path d="M3 11l5 6L19 4" fill="none" stroke="#a2ff00" stroke-width="4"/></svg>Boost course bookings and reduce administrative time and costs</li>
  <li><svg viewBox="0 0 22 22"><path d="M3 11l5 6L19 4" fill="none" stroke="#a2ff00" stroke-width="4"/></svg>Course Admin is Web based meaning you can access your course information from anywhere at any time.</li>
  <li><svg viewBox="0 0 22 22"><path d="M3 11l5 6L19 4" fill="none" stroke="#a2ff00" stroke-width="4"/></svg>System is very intuitive and easy to use.</li>
  <li><svg viewBox="0 0 22 22"><path d="M3 11l5 6L19 4" fill="none" stroke="#a2ff00" stroke-width="4"/></svg>Lighten your workload</li>
  <li><svg viewBox="0 0 22 22"><path d="M3 11l5 6L19 4" fill="none" stroke="#a2ff00" stroke-width="4"/></svg>Upload and manage offline bookings through the admin dashboard</li>
  <li><svg viewBox="0 0 22 22"><path d="M3 11l5 6L19 4" fill="none" stroke="#a2ff00" stroke-width="4"/></svg>Keep your attendees organized all the way up to the course date and beyond</li>
</ul>

<h2 class="contact-title abs">Contact Us Now for a free no obligation discussion about your requirement and quote.</h2>

<div class="form-row abs" style="top:2847px"><label>Name:</label><div class="field"></div></div>
<div class="form-row abs" style="top:2901px"><label>Company:</label><div class="field"></div></div>
<div class="form-row abs" style="top:2952px"><label>Email:</label><div class="field"></div></div>
<div class="form-row abs" style="top:3006px"><label>Telephone:</label><div class="field"></div></div>
<div class="submit abs">SUBMIT</div>

<footer class="footer abs">| ©2010 Brightloom Works. All Rights Reserved | Disclaimer |</footer>
<svg class="footer-mark abs" viewBox="0 0 30 30" fill="none" stroke="#d9ee2c" stroke-width="2.5"><circle cx="15" cy="12" r="8"/><path d="M11 22h8M12 26h6"/></svg>

</body>
</html>
```